Im want a website LIKE KVT's and FieldCrest.com's with product payment options like Trovella's

I need a website LIKE KVT with a header made EXACTLY LIKE THAT OF FIELDCRESTS .

The front page photo should be like that of FIELDCREST's webpage as well.

The name of the website will be called "M.K. (Maravel Key)".

We will be targeting ALL MARKETS in a small town in central Panama and charging businesses "listing fees" like a phone book does but also providing informational blogs, news, and other interesting activities.

THIS IS A MULTI PAGE WEBSITE

THIS IS WHERE KVT's website meets Zentaro/FieldCrest.

Once the layout is built I will tweak and modify, add information, and upload items for sale.

Here is a list of specific categories that should be listed out above the front page header image/search bar

-- Home -- News -- Travel -- Activities -- Shop & Dine -- Store -- More... --

These categories should be spread across the bottom of the page in three sections:

WHATS SO GREAT ABOUT (Maravel Key),
HAND PICKED TOURS
ACTIVITIES etc.

Also lets use www.Trovella.example 's
"HOT DESTINATIONS"
"BEAT THE BEST PRICES IN BOQUETE"
"OCTOBERS INSIDER PICKS"
"TOP DESTINATIONS"
and spread them in four sections side-by-side near the bottom of the page.

Overall I would like to see the finished product to be something LIKE KVT's and FieldCrests.

WE NEED ONLINE PAYMENT OPTIONS LIKE ZENTARO'S WEBSITE HAS

This will be a desktop website but should be very mobile friendly as well.

-roderick

P.S. Good luck!

If it isn't already too late to change the website name, the name of the website should be "Maravel Key". Added Friday, October 9, 2015

What do you guys think the budget should be to win this? Added Saturday, October 10, 2015

www.lunavista.example is the most amazing simple site. Whoever can make me a replica with my specifications will win immediately!!!! Added Sunday, October 18, 2015

OMG www.lunavista.example is the bomb!So simple and elegant. Whoever can make me an EXACT REPLICA OF WWW.LUNAVISTA.EXAMPLE as my site with the specifications mentioned in my brief will take home the $825.00 immediately! Good luck amigos! Added Sunday, October 18, 2015

Does anybody know how to add recurring monthly billing options on this website? Added Sunday, October 18, 2015

ALL MARKETS

Product

Coded - Design and coding required

5+ page

• Paywell payment options.
• I must be able to add and remove photos/text and video from the HTML files in the page.
• Be creative my friends, and may the odds be forever in your favor!
• I added some photos of a good layout for our page below.

```html
<!DOCTYPE html>
<html lang="en">
<head>
<meta charset="utf-8">
<title>Maravel Key</title>
<link href="https://fonts.googleapis.com/css2?family=Montserrat:wght@400;600;700;800&family=Open+Sans:wght@400;600;700&display=swap" rel="stylesheet">
<style>
:root{
  --orange:#f7a21b;
  --yellow:#f6c21c;
  --blue:#1a9ee0;
  --navy:#0e3d5b;
  --ink:#2a2a2a;
  --muted:#8a8a8a;
  --line:#e3e3e3;
  --paper:#ffffff;
  --soft:#f5f5f5;
  --pink:#e8457a;
}
*{box-sizing:border-box;margin:0;padding:0}
html,body{width:1200px;height:2820px;overflow:hidden}
body{font-family:"Open Sans",Arial,sans-serif;color:var(--ink);background:var(--paper);position:relative}
h1,h2,h3,h4,.btn,.nav a,.brand{font-family:"Montserrat",Arial,sans-serif}

/* header */
.site-header{position:absolute;top:0;left:0;width:1200px;height:88px;background:var(--paper);box-shadow:0 2px 6px rgba(0,0,0,.08);z-index:2}
.account-links{position:absolute;top:6px;right:48px;font-size:11px;color:var(--blue)}
.account-links span{margin:0 4px;color:var(--muted)}
.brand{position:absolute;left:48px;top:28px;font-size:30px;font-weight:800;color:var(--orange);letter-spacing:.5px}
.nav{position:absolute;left:452px;top:40px;display:flex;gap:0}
.nav a{display:block;width:130px;height:30px;line-height:30px;text-align:center;font-size:12px;font-weight:600;color:#555;text-decoration:none;letter-spacing:.5px}
.nav a.active{width:80px;margin-right:40px;background:var(--orange);color:#fff;border-radius:2px}

/* hero */
.hero{position:absolute;top:88px;left:0;width:1200px;height:600px;
  background:linear-gradient(180deg,#5fb0e4 0%,#8fcdf0 40%,#57c6d6 62%,#7fd3d8 72%,#e9e3d3 86%,#dcd3bd 100%)}
.hero-text{position:absolute;top:160px;width:100%;text-align:center;color:#fff}
.hero-text h1{font-size:50px;font-weight:800;letter-spacing:3px;text-shadow:0 2px 6px rgba(0,0,0,.25)}
.hero-text p{font-family:"Montserrat",sans-serif;font-size:24px;font-weight:700;margin-top:6px;letter-spacing:1px;text-shadow:0 2px 4px rgba(0,0,0,.25)}
.search{position:absolute;top:270px;left:208px;width:776px;height:58px;background:#fff;border:4px solid rgba(255,255,255,.7);box-shadow:0 2px 8px rgba(0,0,0,.2);display:flex;align-items:center;padding:0 16px;font-size:15px;color:#9a9a9a}
.search svg{position:absolute;right:16px;top:14px}
.hero-cta{position:absolute;top:392px;left:480px;width:240px;height:52px;line-height:52px;text-align:center;background:var(--yellow);color:#222;font-size:18px;font-weight:600;border-radius:3px}

/* tours */
.tours{position:absolute;top:688px;left:0;width:1200px;height:900px;background:var(--soft)}
.section-title{text-align:center;font-size:30px;font-weight:700;color:#222;letter-spacing:1px}
.tours .section-title{margin-top:68px}
.section-sub{text-align:center;font-size:14px;color:var(--muted);margin-top:8px}
.tour-grid{position:absolute;top:144px;left:48px;display:grid;grid-template-columns:repeat(3,352px);column-gap:24px;row-gap:40px}
.tour-card{width:352px;height:280px;background:#fff;box-shadow:0 1px 4px rgba(0,0,0,.12);position:relative}
.tour-photo{position:relative;height:220px}
.tour-tag{position:absolute;left:10px;bottom:8px;font-size:11px;color:#fff;background:rgba(0,0,0,.45);padding:2px 8px}
.tour-price{position:absolute;right:12px;bottom:6px;font-family:"Montserrat",sans-serif;font-size:26px;font-weight:700;color:#fff;text-shadow:0 1px 3px rgba(0,0,0,.5)}
.tour-badge{position:absolute;right:0;top:140px;width:72px;height:72px;background:var(--pink);color:#fff;font-size:11px;font-weight:700;text-align:center;padding-top:20px;line-height:15px}
.tour-info{height:60px;padding:10px 14px;position:relative}
.tour-info h3{font-size:15px;font-weight:700;color:#222}
.stars{font-size:13px;color:var(--yellow);letter-spacing:1px}
.stars i{color:#ccc;font-style:normal}
.tour-info svg{position:absolute;right:14px;top:14px}
.btn{display:inline-block;background:var(--blue);color:#fff;font-size:14px;font-weight:700;text-align:center;border-radius:3px;letter-spacing:.5px}
.view-all{position:absolute;top:808px;left:512px;width:176px;height:40px;line-height:40px}

/* belong */
.belong{position:absolute;top:1588px;left:0;width:1200px;height:452px;
  background:linear-gradient(100deg,#2f5a7a 0%,#4d7f9f 35%,#6d8aa0 60%,#a89582 80%,#c9b7a0 100%)}
.belong::after{content:"";position:absolute;inset:0;background:rgba(10,25,45,.35)}
.belong-text{position:absolute;z-index:1;top:104px;width:100%;text-align:center;color:#fff}
.belong-text h2{font-size:60px;font-weight:800;letter-spacing:2px}
.belong-text p{font-size:15px;font-weight:600;width:560px;margin:12px auto 0;line-height:22px}
.play{position:absolute;z-index:1;top:248px;left:564px}

/* get started */
.get-started{position:absolute;top:2040px;left:0;width:1200px;height:440px;background:#fff}
.laptop{position:absolute;left:48px;top:80px;width:464px;height:290px;border-radius:10px;
  background:linear-gradient(180deg,#3a3a3a 0%,#3a3a3a 6%,#f79a1e 6%,#f7a21b 88%,#d9d9d9 88%,#bdbdbd 100%)}
.start-copy{position:absolute;left:592px;top:100px;width:520px}
.start-copy h2{font-size:34px;font-weight:600;color:#333}
.start-copy p{font-size:15px;color:#666;line-height:22px;margin-top:10px}
.steps{list-style:none;margin-top:22px}
.steps li{font-size:15px;color:#555;line-height:28px;display:flex;align-items:center;gap:10px}
.start-btn{position:absolute;left:608px;top:344px;width:152px;height:40px;line-height:40px}

/* footer */
.site-footer{position:absolute;top:2480px;left:0;width:1200px;height:272px;background:var(--blue);color:#fff}
.foot-col{position:absolute;top:32px}
.foot-col h4{font-size:17px;font-weight:700;letter-spacing:.5px;margin-bottom:14px}
.col-about{left:48px;width:260px}
.col-about p{font-size:13px;line-height:19px}
.outline-btn{display:inline-block;margin-top:14px;border:2px solid #fff;padding:6px 16px;font-size:13px;font-weight:700;font-family:"Montserrat",sans-serif}
.col-contact{left:384px;width:230px}
.contact-row{display:flex;align-items:center;gap:10px;font-size:13px;margin-bottom:12px}
.socials{display:flex;gap:10px;margin-top:10px}
.socials span{width:26px;height:26px;border-radius:50%;background:#0d5f8e;display:block}
.col-gallery{left:656px}
.gallery{display:grid;grid-template-columns:repeat(3,80px);gap:6px}
.gallery div{height:56px}
.col-subscribe{left:912px;width:240px}
.col-subscribe p{font-size:13px;line-height:19px}
.sub-form{display:flex;margin-top:16px}
.sub-form span{flex:1;height:36px;background:#fff;color:#999;font-size:12px;line-height:36px;padding-left:10px}
.sub-form b{width:40px;height:36px;background:var(--orange);color:#fff;line-height:36px;text-align:center;font-size:13px}
.bottom-bar{position:absolute;top:2752px;left:0;width:1200px;height:68px;background:var(--navy);color:#fff;font-size:13px}
.bottom-links{position:absolute;left:48px;top:24px}
.bottom-links span{margin:0 8px;opacity:.6}
.copyright{position:absolute;right:48px;top:24px}
</style>
</head>
<body>

<header class="site-header">
  <div class="account-links">Login<span>|</span>Register</div>
  <div class="brand">Maravel Key</div>
  <nav class="nav">
    <a class="active">HOME</a><a style="width:112px">NEWS</a><a style="width:128px">TRAVEL</a><a style="width:152px">ACTIVITIES</a><a style="width:128px">SHOP &amp; DINE</a><a style="width:60px">STORE</a>
  </nav>
</header>

<section class="hero" role="img" aria-label="Photo of a woman in a red sarong raising her arms on a tropical beach with turquoise sea and blue sky">
  <div class="hero-text">
    <h1>LET THE ACTIVITIES BEGIN!</h1>
    <p>GET 20% DISCOUNT ON SINGLE TOUR PACKAGE</p>
  </div>
  <div class="search">Search for Destinations, attractions and tours
    <svg width="24" height="24" viewBox="0 0 24 24"><circle cx="10" cy="10" r="7" fill="none" stroke="#f6c21c" stroke-width="3"/><line x1="15" y1="15" x2="22" y2="22" stroke="#f6c21c" stroke-width="3.5" stroke-linecap="round"/></svg>
  </div>
  <div class="hero-cta">All Broadway Shows</div>
</section>

<section class="tours">
  <h2 class="section-title">PARIS TOP TOURS</h2>
  <p class="section-sub">Quisque in tortor a libero posuere laoreet vitae sed arcu. Curabitur consequat.</p>
  <div class="tour-grid">
    <article class="tour-card">
      <div class="tour-photo" role="img" aria-label="Photo of the painted dome interior of the Pantheon" style="background:linear-gradient(160deg,#8a6a3c,#c79a55 50%,#6e5230)">
        <span class="tour-badge">TOP<br>RATED</span><span class="tour-tag">Historic tours</span>
      </div>
      <div class="tour-info"><h3>PANTHEON TOUR</h3><div class="stars">★★★★<i>★</i></div>
        <svg width="30" height="30" viewBox="0 0 30 30"><circle cx="15" cy="15" r="13" fill="none" stroke="#ccc" stroke-width="2"/><path d="M11 11h8v9l-4-3-4 3z" fill="#bbb"/></svg></div>
    </article>
    <article class="tour-card">
      <div class="tour-photo" role="img" aria-label="Photo of the Arc de Triomphe under a blue sky" style="background:linear-gradient(180deg,#8fb6d8,#c9c2b2 60%,#8a8170)">
        <span class="tour-tag">Historic tours</span><span class="tour-price">$52</span>
      </div>
      <div class="tour-info"><h3>ARC DE TRIOMPHE</h3><div class="stars">★★★★<i>★</i></div>
        <svg width="30" height="30" viewBox="0 0 30 30"><circle cx="15" cy="15" r="13" fill="none" stroke="#ccc" stroke-width="2"/><path d="M11 11h8v9l-4-3-4 3z" fill="#bbb"/></svg></div>
    </article>
    <article class="tour-card">
      <div class="tour-photo" role="img" aria-label="Photo of a Paris bakery shopfront with gold lettering" style="background:linear-gradient(180deg,#6b3a28,#a7714a 50%,#3c2a20)">
        <span class="tour-tag">Food tours</span><span class="tour-price">$82</span>
      </div>
      <div class="tour-info"><h3>BOULANGERIE TOUR</h3><div class="stars">★★★★<i>★</i></div>
        <svg width="30" height="30" viewBox="0 0 30 30"><circle cx="15" cy="15" r="13" fill="none" stroke="#ccc" stroke-width="2"/><path d="M11 11h8v9l-4-3-4 3z" fill="#bbb"/></svg></div>
    </article>
    <article class="tour-card">
      <div class="tour-photo" role="img" aria-label="Photo of smiling friends on an open top bus" style="background:linear-gradient(160deg,#d9b79a,#9a6e55 50%,#c8c0b5)">
        <span class="tour-tag">Bus tours</span><span class="tour-price">$62</span>
      </div>
      <div class="tour-info"><h3>OPEN BUS TOUR</h3><div class="stars">★★★★<i>★</i></div>
        <svg width="30" height="30" viewBox="0 0 30 30"><circle cx="15" cy="15" r="13" fill="none" stroke="#ccc" stroke-width="2"/><path d="M11 11h8v9l-4-3-4 3z" fill="#bbb"/></svg></div>
    </article>
    <article class="tour-card">
      <div class="tour-photo" role="img" aria-label="Photo of the Louvre palace facade at dusk" style="background:linear-gradient(180deg,#3f6fa8,#7f99b8 45%,#c49a5e 75%,#6b5a40)">
        <span class="tour-tag">Museum tours</span><span class="tour-price">$102</span>
      </div>
      <div class="tour-info"><h3>LOUVRE MUSEUM TOUR</h3><div class="stars">★★★★<i>★</i></div>
        <svg width="30" height="30" viewBox="0 0 30 30"><circle cx="15" cy="15" r="13" fill="none" stroke="#ccc" stroke-width="2"/><path d="M11 11h8v9l-4-3-4 3z" fill="#bbb"/></svg></div>
    </article>
    <article class="tour-card">
      <div class="tour-photo" role="img" aria-label="Photo of the Eiffel Tower against a bright sky" style="background:linear-gradient(180deg,#4d8ccc,#9cc3e4 55%,#7a6a50)">
        <span class="tour-tag">City sightseeing</span><span class="tour-price">$49</span>
      </div>
      <div class="tour-info"><h3>TOUR EIFFEL TOUR</h3><div class="stars">★★★★<i>★</i></div>
        <svg width="30" height="30" viewBox="0 0 30 30"><circle cx="15" cy="15" r="13" fill="none" stroke="#ccc" stroke-width="2"/><path d="M11 11h8v9l-4-3-4 3z" fill="#bbb"/></svg></div>
    </article>
  </div>
  <div class="btn view-all">VIEW ALL TOURS</div>
</section>

<section class="belong" role="img" aria-label="Photo of a colourful hillside seaside town above a blue harbour">
  <div class="belong-text">
    <h2>BELONG ANYWHERE</h2>
    <p>Lorem ipsum dolor sit amet, vix erat audiam ei. Cum doctus civibus efficiantur in. Nec id tempor imperdiet deterruisset.</p>
  </div>
  <svg class="play" width="72" height="72" viewBox="0 0 72 72"><circle cx="36" cy="36" r="33" fill="rgba(0,0,0,.25)" stroke="#fff" stroke-width="4"/><path d="M28 22l22 14-22 14z" fill="#fff"/></svg>
</section>

<section class="get-started">
  <div class="laptop" role="img" aria-label="Laptop showing the Town Trails app screen with an orange city skyline illustration"></div>
  <div class="start-copy">
    <h2>Get started with TownTrails</h2>
    <p>Lorem ipsum dolor sit amet, vix erat audiam ei. Cum doctus civibus efficiantur in. Nec id tempor imperdiet deterruisset.</p>
    <ul class="steps">
      <li><svg width="12" height="12" viewBox="0 0 12 12"><path d="M3 1l6 5-6 5z" fill="#1a9ee0"/></svg>Select your preferred tours</li>
      <li><svg width="12" height="12" viewBox="0 0 12 12"><path d="M3 1l6 5-6 5z" fill="#1a9ee0"/></svg>Purchase tickets and options</li>
      <li><svg width="12" height="12" viewBox="0 0 12 12"><path d="M3 1l6 5-6 5z" fill="#1a9ee0"/></svg>Pick them directly from your office</li>
    </ul>
  </div>
  <div class="btn start-btn">START NOW</div>
</section>

<footer class="site-footer">
  <div class="foot-col col-about">
    <h4>ABOUT</h4>
    <p>Lorem Ipsum is simply dummy text of the printing and typesetting industry. Lorem Ipsum has been the industry's standard dummy text ever since the 1500s.</p>
    <span class="outline-btn">VIEW MORE</span>
  </div>
  <div class="foot-col col-contact">
    <h4>CONTACT US</h4>
    <div class="contact-row"><svg width="14" height="18" viewBox="0 0 14 18"><path d="M7 0a7 7 0 0 0-7 7c0 5 7 11 7 11s7-6 7-11a7 7 0 0 0-7-7z" fill="#fff"/><circle cx="7" cy="7" r="2.5" fill="#1a9ee0"/></svg>Calle 4 #12, Maravel Key</div>
    <div class="contact-row"><svg width="16" height="12" viewBox="0 0 16 12"><rect width="16" height="12" rx="1" fill="#fff"/><path d="M1 1l7 6 7-6" fill="none" stroke="#1a9ee0" stroke-width="1.5"/></svg>hello@maravelkey.example</div>
    <div class="contact-row"><svg width="14" height="14" viewBox="0 0 14 14"><path d="M3 0l3 3-2 2c1 2 3 4 5 5l2-2 3 3-2 3C6 14 0 8 0 3z" fill="#fff"/></svg>+507 555 0142</div>
    <div class="socials"><span></span><span></span><span></span><span></span></div>
  </div>
  <div class="foot-col col-gallery">
    <h4>GALLERY</h4>
    <div class="gallery" role="img" aria-label="Six small travel photo thumbnails">
      <div style="background:#d9a35a"></div><div style="background:#4f86b8"></div><div style="background:#8a6b4a"></div>
      <div style="background:#5a9bc9"></div><div style="background:#c27a4a"></div><div style="background:#3f6d8f"></div>
    </div>
  </div>
  <div class="foot-col col-subscribe">
    <h4>SUBSCRIBE</h4>
    <p>Don't miss any deal. Subscribe to get offers alerts.</p>
    <div class="sub-form"><span>Enter Email Here</span><b>GO</b></div>
  </div>
</footer>

<div class="bottom-bar">
  <div class="bottom-links">Home<span>|</span>News<span>|</span>Travel<span>|</span>Activities<span>|</span>Shop &amp; Dine<span>|</span>Store</div>
  <div class="copyright">© 1991-2015 Maravel Key, Inc. All rights reserved.</div>
</div>

</body>
</html>
```